Eavestone screen porch

Can you please design a flyer for me promoting my screen porch businessPlease remove the seamless gutters word from the title and add “screen porches” I have added the logo and a bunch of pictures from projects that I have done in the past. You can use words like Hillcrest Screen porches, etc

Target Market(s)

homeowners, contractors, builders

Industry/Entity Type

Construction

Requirements
Must have
• Dov Kerring
• Eavestone Gutters
• 2937 Old Hwy 52 N, Greer, SC 29607
• 864-307-6184
Nice to have
• A few colors maybe 3 most
• nice looking font

```html
<!DOCTYPE html>
<html lang="en">
<head>
<meta charset="utf-8">
<title>Hillcrest Screen Porches Flyer</title>
<link href="https://fonts.googleapis.com/css2?family=Roboto:ital,wght@0,400;0,500;0,700;0,900;1,500&display=swap" rel="stylesheet">
<style>
  :root {
    --red: #e3161f;
    --black: #0d0d0d;
    --white: #ffffff;
    --text-grey: #4a4a4a;
    --stage: #e4e4e4;
  }
  * { margin: 0; padding: 0; box-sizing: border-box; }
  html, body { width: 1200px; height: 800px; overflow: hidden; }
  body {
    background: var(--stage);
    font-family: "Roboto", Arial, sans-serif;
    position: relative;
  }
  .flyer {
    position: absolute;
    left: 340px; top: 32px;
    width: 520px; height: 736px;
    background: var(--white);
    overflow: hidden;
    box-shadow: 0 6px 24px rgba(0,0,0,.18);
  }
  .hero-photo {
    position: absolute; left: 0; top: 0; width: 520px; height: 345px;
    background: linear-gradient(160deg, #9a9a9a 0%, #c9c9c9 35%, #7b7b7b 70%, #3e3e3e 100%);
  }
  .hero-shade {
    position: absolute; left: 240px; top: 0; width: 280px; height: 345px;
    background: linear-gradient(90deg, rgba(13,13,13,0) 0%, rgba(13,13,13,.85) 30%, var(--black) 60%);
  }
  .top-band { position: absolute; left: 0; top: 0; width: 520px; height: 16px; background: var(--black); }
  .logo-box {
    position: absolute; left: 38px; top: 0; width: 132px; height: 94px;
    background: var(--white);
    display: flex; align-items: center; justify-content: center; text-align: center;
  }
  .logo-name { color: var(--red); font-weight: 900; font-size: 19px; line-height: 1.05; text-transform: uppercase; }
  .contact-tab {
    position: absolute; left: 296px; top: 16px; width: 224px; height: 84px;
    background: var(--red);
    clip-path: polygon(28px 0, 100% 0, 100% 100%, 0 100%, 0 44px);
    color: var(--white);
  }
  .contact-notch {
    position: absolute; left: 262px; top: 16px; width: 40px; height: 44px;
    background: var(--white);
    clip-path: polygon(100% 0, 100% 100%, 0 100%);
  }
  .contact-label { position: absolute; left: 78px; top: 14px; font-weight: 700; font-size: 15px; color: var(--black); }
  .contact-icon { position: absolute; left: 38px; top: 10px; }
  .contact-phone { position: absolute; left: 38px; top: 45px; font-weight: 700; font-size: 21px; letter-spacing: .3px; }
  .headline {
    position: absolute; right: 28px; top: 120px;
    color: var(--white); font-weight: 700; font-size: 31px; line-height: 1.03;
    text-align: right; text-transform: uppercase;
  }
  .headline-rule { position: absolute; left: 345px; top: 232px; width: 150px; height: 4px; background: var(--red); }
  .headline-sub {
    position: absolute; right: 28px; top: 246px;
    color: var(--white); font-weight: 700; font-size: 13px; line-height: 1.25;
    text-align: right; text-transform: uppercase;
  }
  .project-photo {
    position: absolute; left: 278px; width: 226px;
    background: linear-gradient(150deg, #d9d9d9 0%, #8c8c8c 55%, #454545 100%);
  }
  .project-photo.first { top: 348px; height: 140px; }
  .project-photo.second { top: 502px; height: 152px; background: linear-gradient(160deg, #bdbdbd 0%, #5e5e5e 60%, #2a2a2a 100%); }
  .intro { position: absolute; left: 18px; top: 362px; width: 250px; }
  .intro-title { color: var(--red); font-weight: 700; font-size: 16px; margin-bottom: 7px; text-transform: uppercase; white-space: nowrap; }
  .intro p { color: var(--text-grey); font-size: 10.8px; line-height: 1.33; text-align: justify; margin-bottom: 10px; }
  .benefits {
    position: absolute; left: 18px; top: 588px; width: 250px; height: 70px;
    background: var(--black); color: var(--white); padding: 9px 14px;
  }
  .benefits-title { font-weight: 700; font-size: 12.5px; margin-bottom: 6px; white-space: nowrap; }
  .benefits-list { list-style: none; display: grid; grid-template-columns: 96px 1fr; row-gap: 3px; column-gap: 6px; }
  .benefits-list li { display: flex; align-items: center; gap: 5px; font-size: 9px; font-style: italic; font-weight: 500; white-space: nowrap; }
  .benefits-list svg { flex: none; }
  .footer-web {
    position: absolute; left: 0; top: 665px; width: 245px; height: 71px;
    background: var(--red); color: var(--white); padding: 12px 0 0 20px;
  }
  .footer-web .line { display: flex; align-items: center; gap: 9px; font-size: 11.5px; margin-bottom: 9px; white-space: nowrap; }
  .footer-address {
    position: absolute; left: 245px; top: 665px; width: 275px; height: 71px;
    background: var(--black); color: var(--white); padding: 12px 0 0 52px;
  }
  .footer-address .pin { position: absolute; left: 24px; top: 16px; }
  .rep-name { color: var(--red); font-weight: 700; font-size: 11.5px; }
  .rep-address { font-size: 10px; line-height: 1.2; }
  .social { position: absolute; top: 20px; width: 22px; height: 22px; border-radius: 50%; background: var(--white); }
  .social.one { left: 190px; }
  .social.two { left: 219px; }
</style>
</head>
<body>
  <main class="flyer">
    <div class="hero-photo" role="img" aria-label="Photo of a house with a screened-in porch and white staircase"></div>
    <div class="hero-shade"></div>
    <div class="top-band"></div>

    <div class="logo-box"><span class="logo-name">Eavestone Gutters</span></div>

    <div class="contact-notch"></div>
    <div class="contact-tab">
      <svg class="contact-icon" width="34" height="30" viewBox="0 0 34 30" aria-hidden="true">
        <path d="M4 3h18a2 2 0 0 1 2 2v10a2 2 0 0 1-2 2H11l-6 5v-5H4a2 2 0 0 1-2-2V5a2 2 0 0 1 2-2z" fill="none" stroke="#0d0d0d" stroke-width="2.4"/>
        <path d="M27 9h3a2 2 0 0 1 2 2v9a2 2 0 0 1-2 2h-1v5l-6-5h-7" fill="none" stroke="#0d0d0d" stroke-width="2.4"/>
        <circle cx="8" cy="10" r="1.6" fill="#0d0d0d"/><circle cx="13" cy="10" r="1.6" fill="#0d0d0d"/><circle cx="18" cy="10" r="1.6" fill="#0d0d0d"/>
      </svg>
      <span class="contact-label">CONTACT US:</span>
      <span class="contact-phone">864-307-6184</span>
    </div>

    <h1 class="headline">Hillcrest<br>Screen<br>Porches</h1>
    <div class="headline-rule"></div>
    <p class="headline-sub">Screened-in porch<br>enclosures in Greenville,<br>Spartanburg and beyond!</p>

    <div class="project-photo first" role="img" aria-label="Photo of a gabled screened porch addition"></div>
    <div class="project-photo second" role="img" aria-label="Photo of an elevated screened porch with cable railing"></div>

    <section class="intro">
      <h2 class="intro-title">Why a screened-in porch?</h2>
      <p>Screen porch enclosures are beneficial to homes as they provide a quiet place to enjoy a good book, entertain friends and family at your next dinner party, or give the kids a safe place to play. What are some great things you could do with a screened in porch?</p>
      <p>If you're in Greenville, Spartanburg, or surrounding areas, call Eavestone Gutters today to start your project. We make homes more functional and comfortable, one screened in porch at a time!</p>
    </section>

    <section class="benefits">
      <h3 class="benefits-title">Benefits of Screened in Porches:</h3>
      <ul class="benefits-list">
        <li><svg width="10" height="10" viewBox="0 0 10 10"><circle cx="5" cy="5" r="5" fill="#e3161f"/><path d="M2.6 5.2l1.6 1.6 3.2-3.4" stroke="#fff" stroke-width="1.3" fill="none"/></svg>Year-Round Use</li>
        <li><svg width="10" height="10" viewBox="0 0 10 10"><circle cx="5" cy="5" r="5" fill="#e3161f"/><path d="M2.6 5.2l1.6 1.6 3.2-3.4" stroke="#fff" stroke-width="1.3" fill="none"/></svg>No Bugs</li>
        <li><svg width="10" height="10" viewBox="0 0 10 10"><circle cx="5" cy="5" r="5" fill="#e3161f"/><path d="M2.6 5.2l1.6 1.6 3.2-3.4" stroke="#fff" stroke-width="1.3" fill="none"/></svg>New Family Space</li>
        <li><svg width="10" height="10" viewBox="0 0 10 10"><circle cx="5" cy="5" r="5" fill="#e3161f"/><path d="M2.6 5.2l1.6 1.6 3.2-3.4" stroke="#fff" stroke-width="1.3" fill="none"/></svg>Home Value</li>
        <li><svg width="10" height="10" viewBox="0 0 10 10"><circle cx="5" cy="5" r="5" fill="#e3161f"/><path d="M2.6 5.2l1.6 1.6 3.2-3.4" stroke="#fff" stroke-width="1.3" fill="none"/></svg>Privacy</li>
        <li><svg width="10" height="10" viewBox="0 0 10 10"><circle cx="5" cy="5" r="5" fill="#e3161f"/><path d="M2.6 5.2l1.6 1.6 3.2-3.4" stroke="#fff" stroke-width="1.3" fill="none"/></svg>Extend Your Living Space</li>
      </ul>
    </section>

    <footer>
      <div class="footer-web">
        <div class="line">
          <svg width="16" height="16" viewBox="0 0 16 16"><circle cx="8" cy="8" r="8" fill="#fff"/><g stroke="#e3161f" stroke-width="1.1" fill="none"><circle cx="8" cy="8" r="5"/><ellipse cx="8" cy="8" rx="2.2" ry="5"/><path d="M3 8h10"/></g></svg>
          www.eavestoneseamlessgutters.com
        </div>
        <div class="line">
          <svg width="16" height="16" viewBox="0 0 16 16"><circle cx="8" cy="8" r="8" fill="#fff"/><rect x="4" y="5" width="8" height="6" fill="none" stroke="#e3161f" stroke-width="1.1"/><path d="M4 5l4 3.2L12 5" fill="none" stroke="#e3161f" stroke-width="1.1"/></svg>
          info@eavestonegutters.com
        </div>
      </div>
      <div class="footer-address">
        <svg class="pin" width="16" height="20" viewBox="0 0 16 20"><path d="M8 0a8 8 0 0 1 8 8c0 5-8 12-8 12S0 13 0 8a8 8 0 0 1 8-8z" fill="#e3161f"/><circle cx="8" cy="8" r="3" fill="#0d0d0d"/></svg>
        <div class="rep-name">Dov Kerring</div>
        <div class="rep-address">Eavestone Gutters<br>2937 Old Highway 52<br>North, Greer, SC 29607</div>
        <span class="social one"></span>
        <span class="social two"></span>
      </div>
    </footer>
  </main>
</body>
</html>
```